Meridian Clearsound Wellness LLC Card Design

Need business card with a logo for a hearing aid sales and audiology business. We have two Hearing Instrument Specialists and one Audiologist on staff. Over 25 years in business. Locally owned and operated. Financing available. Most insurances accepted.

Meridian Clearsound Wellness LLC
48730 W Larkfield, Suite 9
Spokane, WA 99371
509-617-2084
www.meridianclearsound-example.com

Manager
Tobias Wrenfield HIS COHC
License #81957260

Target Market(s)

50yr old + people with a hearing loss.

Industry/Entity Type

Business

Contact Information for Business Card

48730 W Larkfield, Suite 9
Spokane, WA 99371
509-617-2084
www.meridianclearsound-example.com

Manager
Tobias Wrenfield HIS COHC
RTEQ #81957260

Font styles to use
Serif
Sans Serif

Requirements
Must have
• Business name, Tobias's name and title(s) and contact information, License #, web address
Nice to have
Should not have

```html
<!DOCTYPE html>
<html lang="en">
<head>
<meta charset="utf-8">
<title>Meridian Clearsound Wellness LLC – Business Card</title>
<link rel="stylesheet" href="https://fonts.googleapis.com/css2?family=Alegreya+Sans:ital,wght@0,500;0,700;1,400&family=Alegreya+Sans+SC:wght@500&family=Open+Sans:wght@400&display=swap">
<style>
  :root {
    --navy: #2d4f9f;
    --navy-dark: #2a4a8e;
    --sky: #0a98dc;
    --sky-text: #1b9bd8;
    --paper: #ffffff;
  }
  html, body {
    margin: 0;
    padding: 0;
    width: 1200px;
    height: 758px;
    overflow: hidden;
    background: var(--paper);
  }
  .card {
    position: relative;
    width: 1200px;
    height: 758px;
    background: var(--paper);
    font-family: "Alegreya Sans", sans-serif;
    overflow: hidden;
  }
  .brand-square {
    position: absolute;
    left: 68px;
    top: 0;
    width: 185px;
    height: 265px;
    background: var(--navy);
  }
  .brand-name {
    position: absolute;
    left: 280px;
    top: 92px;
    margin: 0;
    font-family: "Alegreya Sans", sans-serif;
    font-weight: 500;
    font-size: 50px;
    line-height: 1;
    color: var(--sky-text);
    white-space: nowrap;
  }
  .rule {
    position: absolute;
    height: 3px;
    background: var(--navy);
  }
  .rule--upper { left: 356px; width: 675px; top: 170px; }
  .rule--lower { left: 378px; width: 633px; top: 180px; }

  .person {
    position: absolute;
    left: 66px;
    top: 378px;
  }
  .person__name {
    margin: 0;
    font-weight: 700;
    font-size: 50px;
    line-height: 1;
    color: var(--navy-dark);
    white-space: nowrap;
  }
  .person__role {
    margin: 4px 0 0 37px;
    white-space: nowrap;
    line-height: 1;
  }
  .person__title {
    font-family: "Alegreya Sans SC", sans-serif;
    font-weight: 500;
    font-size: 44px;
    color: var(--sky-text);
  }
  .person__license {
    font-style: italic;
    font-weight: 400;
    font-size: 22px;
    color: var(--sky-text);
    margin-left: 6px;
  }

  .contact {
    position: absolute;
    left: 680px;
    top: 376px;
    font-family: "Alegreya Sans SC", sans-serif;
    font-weight: 500;
    color: var(--navy-dark);
    font-size: 34px;
    line-height: 1;
  }
  .contact__row {
    position: relative;
    padding-left: 64px;
    white-space: nowrap;
  }
  .contact__row svg {
    position: absolute;
    left: 0;
    top: 0;
  }
  .contact__row--phone { height: 44px; padding-top: 6px; }
  .contact__row--address { margin-top: 20px; line-height: 43px; }
  .contact__row--address svg { top: 8px; }

  .band {
    position: absolute;
    left: 0;
    top: 624px;
    width: 1200px;
    height: 134px;
    background: var(--sky);
  }
  .web {
    position: absolute;
    right: 32px;
    top: 33px;
    height: 68px;
    padding: 0 24px 0 90px;
    display: flex;
    align-items: center;
    background: linear-gradient(90deg, var(--sky) 0%, var(--navy) 55%, var(--navy) 100%);
    font-family: "Open Sans", sans-serif;
    font-size: 30px;
    color: var(--paper);
    white-space: nowrap;
  }
</style>
</head>
<body>
<main class="card">
  <div class="brand-square" aria-hidden="true"></div>
  <h1 class="brand-name">Meridian Clearsound Wellness LLC</h1>
  <div class="rule rule--upper"></div>
  <div class="rule rule--lower"></div>

  <section class="person">
    <p class="person__name">Tobias Wrenfield HIS COHC</p>
    <p class="person__role">
      <span class="person__title">Manager</span><span class="person__license">(RTEQ #81957260)</span>
    </p>
  </section>

  <section class="contact">
    <div class="contact__row contact__row--phone">
      <svg width="54" height="42" viewBox="0 0 54 42" aria-hidden="true">
        <path d="M2 12 C4 3 50 3 52 12 L52 16 L40 16 L40 10 L14 10 L14 16 L2 16 Z" fill="#2a4a8e"/>
        <path d="M12 18 L42 18 L50 40 L4 40 Z" fill="#2a4a8e"/>
        <g fill="#ffffff">
          <rect x="21" y="23" width="3" height="3"/><rect x="26" y="23" width="3" height="3"/><rect x="31" y="23" width="3" height="3"/>
          <rect x="21" y="28" width="3" height="3"/><rect x="26" y="28" width="3" height="3"/><rect x="31" y="28" width="3" height="3"/>
          <rect x="21" y="33" width="3" height="3"/><rect x="26" y="33" width="3" height="3"/><rect x="31" y="33" width="3" height="3"/>
        </g>
      </svg>
      Tel: 509-617-2084
    </div>
    <div class="contact__row contact__row--address">
      <svg width="52" height="50" viewBox="0 0 52 50" aria-hidden="true">
        <path d="M26 2 L51 24 L46 29 L26 11 L6 29 L1 24 Z" fill="#2a4a8e"/>
        <path d="M9 28 L26 14 L43 28 L43 48 L31 48 L31 35 L21 35 L21 48 L9 48 Z" fill="#2a4a8e"/>
      </svg>
      48730 W Larkfield, Suite 9<br>
      Spokane, WA 99371
    </div>
  </section>

  <footer class="band">
    <div class="web">www.meridianclearsound-example.com</div>
  </footer>
</main>
</body>
</html>
```